App Redesign for PathMentor

We're looking for a skilled UI/UX designer to modernize the PathMentor mobile app, enhancing user engagement while preserving our current brand identity.

Key Objectives:
Refresh the app using modern design trends
Maintain a clean, calm, and playful aesthetic aligned with our brand
Boost engagement through improved flow, visuals, and interactivity

Design Requirements:
Retain recognizability from our app and website (see Brand ID Guide) (and website pathmentorhub.example)
Reflect a tone that is supportive, fun/ playful, and professional

Design 5–8 key screens, including:
Home/Dashboard
Daily Intentions Interface
Gamification Overview (Streaks, Rewards)
Social Features (Direct Realtime Feedback, Messaging, Challenges)
Progress Tracking

New Feature Concepts to Include:
Daily Intentions with voice/text input and visual encouragement
Gamification elements like streaks, badges, and animations
Social Connections including messaging, reactions, and feedback tools
Optional: Subtle design cues for future AI-driven interactions

Audience: Adults aged 25–55 interested in personal development and coaching. Tech-comfortable but not tech-savvy.

Visual Inspiration: Wordivo (gamification), Calmnest (intentions), Runqo (social support)

Target Market(s)

Corporate Leaders and Entrepreneurs

Industry/Entity Type

Leadership Training & Consultancies

Font styles to use
Sans Serif
Other font styles liked:
• Avenir, Arial

Colors
FFF300
FFF600
FEFA6F
FFFEC7
FFFEE8

Requirements
Nice to have
• Wordivo, Calmnest,

```html
<!DOCTYPE html>
<html lang="en">
<head>
<meta charset="utf-8">
<title>PathMentor App Screens</title>
<link rel="stylesheet" href="https://fonts.googleapis.com/css2?family=Poppins:ital,wght@0,300;0,400;0,500;0,600;0,700;0,800;1,400;1,700;1,800&display=swap">
<style>
:root{
  --stage:#b3b3b3;
  --yellow:#ffd600;
  --yellow-soft:#fff300;
  --ink:#111111;
  --white:#ffffff;
  --card-grey-a:#bdbab6;
  --card-grey-b:#8e8c8a;
  --line:#444444;
  --muted:#cfcfcf;
}
*{box-sizing:border-box;margin:0;padding:0}
html,body{width:963px;height:1200px;overflow:hidden;background:var(--stage)}
body{position:relative;font-family:'Poppins',Arial,sans-serif;color:var(--white);font-size:7px;line-height:1.3}
.screen{position:absolute;width:200px;height:355px;border-radius:17px;overflow:hidden;
  background:linear-gradient(180deg,#3c3c3c 0%,#0a0a0a 45%,#000 100%)}
.screen.fade-up{background:linear-gradient(180deg,#1c1c1c 0%,#000 18%,#2a2a2a 60%,#4a4a4a 100%)}
.abs{position:absolute}
.status{position:absolute;top:14px;left:16px;right:14px;display:flex;justify-content:space-between;align-items:center;font-size:5.8px;font-weight:600}
.status .net{display:flex;align-items:center;gap:3px}
.battery{width:11px;height:6px;border:1px solid #fff;border-radius:1.5px;position:relative}
.battery::before{content:"";position:absolute;left:1px;top:1px;width:4px;height:2px;background:#fff}
.title{position:absolute;left:0;right:0;text-align:center;font-weight:800;font-style:italic;font-size:12.5px}
.title-left{position:absolute;left:15px;font-weight:800;font-style:italic;font-size:12.5px}
.sub{font-size:5.2px;font-style:italic;color:#ddd}
.viewall{position:absolute;right:14px;font-size:5.2px;font-style:italic;color:#ddd}
.menu{position:absolute;right:14px;top:41px;width:10px;height:8px;border-top:1.5px solid #ccc;border-bottom:1.5px solid #ccc}
.menu::after{content:"";position:absolute;left:0;right:0;top:2px;border-top:1.5px solid #ccc}
/* nav */
.nav{position:absolute;left:0;right:0;bottom:0;height:35px;background:#000;border-top:1px solid #3a3a3a;display:flex}
.nav-item{flex:1;display:flex;flex-direction:column;align-items:center;justify-content:center;gap:2px;border-left:1px solid var(--line)}
.nav-item:first-child{border-left:none}
.nav-item svg{width:13px;height:13px;color:#fff}
.nav-item span{font-size:4.4px;color:var(--yellow);letter-spacing:.1px;white-space:nowrap}
.nav.plain .nav-item svg{width:14px;height:14px;color:#c9a800}
/* login */
.field{position:absolute;left:33px;width:133px;height:18px;border-radius:9px;background:#fff;color:#777;font-size:5.6px;padding-left:15px;line-height:18px}
.btn{position:absolute;border-radius:10px;background:var(--yellow);color:var(--ink);font-weight:600;text-align:center}
/* cards */
.grey-card{position:absolute;border-radius:10px;background:linear-gradient(135deg,var(--card-grey-a),var(--card-grey-b));color:var(--ink);font-size:7px;line-height:1.25}
.day{position:absolute;width:32px;height:32px;border-radius:50%;background:var(--yellow);color:var(--ink);font-weight:700;font-size:15px;display:flex;align-items:center;justify-content:center}
.dots{position:absolute;width:0;border-left:1px dashed #888}
.time-pill{display:block;width:fit-content;background:#fff;border-radius:6px;font-size:3.8px;line-height:1.4;font-weight:600;padding:1px 5px;margin-bottom:4px}
.card-text{font-size:7.4px;font-weight:600;line-height:1.22}
.badge-num{position:absolute;right:5px;top:5px;width:10px;height:10px;border-radius:50%;background:var(--yellow);font-size:4.2px;font-weight:700;display:flex;align-items:center;justify-content:center}
.show{display:block;width:fit-content;background:var(--yellow);border-radius:5px;font-size:3.8px;line-height:1.3;font-weight:700;padding:1.5px 5px;margin-top:4px}
/* messages */
.msg-card{position:absolute;left:22px;width:155px;height:47px;border-radius:24px;background:linear-gradient(90deg,#c9c6c2,#8a8886);color:var(--ink)}
.avatar{position:absolute;border-radius:50%;background:linear-gradient(180deg,#eeeeee,#b5b5b5)}
.msg-card .avatar{left:8px;top:7px;width:33px;height:33px}
.msg-card b{position:absolute;left:52px;top:6px;font-size:9.5px;font-weight:600}
.msg-card p{position:absolute;left:52px;top:22px;font-size:5px;line-height:1.45}
.bubble{position:absolute;background:#efebe8;color:var(--ink);font-size:5px;line-height:1.5;border-radius:4px;padding:5px 10px}
.bubble small{position:absolute;right:5px;bottom:2px;font-size:2.8px;color:#999}
/* gamification */
.yellow-card{position:absolute;background:var(--yellow);border-radius:10px;color:var(--ink)}
.sec{position:absolute;left:25px;font-size:8px;font-weight:800;font-style:italic}
.badge-ico{position:absolute;width:20px;height:20px;border-radius:50%;background:#111;border:1px solid #666;display:flex;align-items:center;justify-content:center;color:#fff;font-weight:700;font-size:11px}
.badge-lbl{position:absolute;font-size:3.6px;text-align:center;line-height:1.1;font-weight:600;width:30px}
</style>
</head>
<body>

<svg width="0" height="0" style="position:absolute">
  <defs>
    <symbol id="i-home" viewBox="0 0 24 24"><path d="M3 11 12 3l9 8v10h-6v-6H9v6H3z" fill="none" stroke="currentColor" stroke-width="1.6" stroke-linejoin="round"/></symbol>
    <symbol id="i-questions" viewBox="0 0 24 24"><path d="M4 4h16v12H10l-4 4v-4H4z" fill="none" stroke="currentColor" stroke-width="1.5" stroke-linejoin="round"/><text x="12" y="13.5" font-size="9" text-anchor="middle" fill="currentColor" font-family="Arial">?</text></symbol>
    <symbol id="i-game" viewBox="0 0 24 24"><rect x="3" y="10" width="18" height="10" rx="5" fill="none" stroke="currentColor" stroke-width="1.4"/><path d="M7 15h4M9 13v4M5 8l2-3M19 8l-2-3M12 8V4M9 7l-1-2M15 7l1-2" stroke="currentColor" stroke-width="1.2" fill="none"/><circle cx="15.5" cy="14" r="1" fill="currentColor"/><circle cx="17.5" cy="16" r="1" fill="currentColor"/></symbol>
    <symbol id="i-people" viewBox="0 0 24 24"><rect x="5" y="2" width="10" height="5" rx="1" fill="none" stroke="currentColor" stroke-width="1.2"/><rect x="11" y="5" width="9" height="4" rx="1" fill="none" stroke="currentColor" stroke-width="1.2"/><circle cx="8" cy="13" r="2.5" fill="none" stroke="currentColor" stroke-width="1.3"/><circle cx="16" cy="13" r="2.5" fill="none" stroke="currentColor" stroke-width="1.3"/><path d="M3 22c0-3 2-5 5-5s5 2 5 5M11 22c0-3 2-5 5-5s5 2 5 5" fill="none" stroke="currentColor" stroke-width="1.3"/></symbol>
    <symbol id="i-more" viewBox="0 0 24 24"><rect x="3" y="3" width="7" height="7" rx="1.5" fill="none" stroke="currentColor" stroke-width="1.5"/><rect x="14" y="3" width="7" height="7" rx="1.5" fill="none" stroke="currentColor" stroke-width="1.5"/><rect x="3" y="14" width="7" height="7" rx="1.5" fill="none" stroke="currentColor" stroke-width="1.5"/><path d="M17.5 14v7M14 17.5h7" stroke="currentColor" stroke-width="1.5"/></symbol>
    <symbol id="i-heart" viewBox="0 0 24 24"><path d="M12 20S3 14 3 8.5A4.5 4.5 0 0 1 12 6a4.5 4.5 0 0 1 9 2.5C21 14 12 20 12 20z" fill="none" stroke="currentColor" stroke-width="1.5"/></symbol>
    <symbol id="i-chat" viewBox="0 0 24 24"><path d="M3 5h18v12h-9l-4 3v-3H3z" fill="none" stroke="currentColor" stroke-width="1.5" stroke-linejoin="round"/></symbol>
    <symbol id="i-user" viewBox="0 0 24 24"><circle cx="12" cy="8" r="4" fill="none" stroke="currentColor" stroke-width="1.5"/><path d="M4 21c0-4 4-7 8-7s8 3 8 7" fill="none" stroke="currentColor" stroke-width="1.5"/></symbol>
    <symbol id="i-cal" viewBox="0 0 24 24"><rect x="3" y="5" width="18" height="16" rx="2" fill="none" stroke="currentColor" stroke-width="2"/><path d="M3 10h18M8 2v5M16 2v5" stroke="currentColor" stroke-width="2"/></symbol>
    <symbol id="i-cal-grid" viewBox="0 0 24 24"><rect x="3" y="5" width="18" height="16" rx="2" fill="none" stroke="currentColor" stroke-width="2"/><path d="M3 10h18M8 2v5M16 2v5M3 14h18M3 18h18M8 10v11M12 10v11M16 10v11" stroke="currentColor" stroke-width="1.4"/></symbol>
  </defs>
</svg>

<!-- ============ ROW 1 ============ -->

<section class="screen login" style="left:37px;top:37px">
  <div class="status"><span>7.00 PM</span><span class="net">▂▄▆ 4G <i class="battery"></i></span></div>
  <div class="abs" style="left:0;right:0;top:116px;display:flex;justify-content:center;align-items:center;gap:6px">
    <span style="width:12px;height:12px;border-radius:50%;background:var(--yellow)"></span>
    <span style="font-size:20px;font-weight:700;color:var(--yellow)">PathMentor</span>
  </div>
  <div class="field" style="top:236px">Username</div>
  <div class="field" style="top:262px">Password</div>
  <div class="btn" style="left:33px;width:133px;top:288px;height:18px;line-height:18px;font-size:5.8px;font-weight:400">Sign In</div>
  <div class="abs" style="left:100px;top:316px;font-size:5.8px;font-style:italic">Forgot password?</div>
</section>

<section class="screen" style="left:267px;top:37px">
  <div class="status"><span>7.00 PM</span><span class="net">▂▄▆ 4G <i class="battery"></i></span></div>
  <h1 class="abs" style="left:16px;top:196px;font-size:17px;line-height:1.3;font-weight:800;font-style:italic">Get Better<br>Result Today!</h1>
  <p class="abs" style="left:16px;top:244px;width:122px;font-size:4.6px;line-height:1.6">Lorem ipsum dolor sit amet, consectetuer adi-piscing elit, sed diam nonummy nibh euismod tincidunt ut laoreet dolore</p>
  <div class="btn" style="left:16px;top:278px;width:71px;height:16px;line-height:16px;font-size:6.4px;font-weight:800;font-style:italic">Start Now</div>
  <nav class="nav">
    <div class="nav-item"><svg><use href="#i-home"/></svg><span>HOME</span></div>
    <div class="nav-item"><svg><use href="#i-questions"/></svg><span>QUESTIONS</span></div>
    <div class="nav-item"><svg><use href="#i-game"/></svg><span>GAMIFICATION</span></div>
    <div class="nav-item"><svg><use href="#i-people"/></svg><span>SOCIAL CHAT</span></div>
    <div class="nav-item"><svg><use href="#i-more"/></svg><span>MORE</span></div>
  </nav>
</section>

<section class="screen" style="left:496px;top:37px">
  <div class="status"><span>7.00 PM</span><span class="net">▂▄▆ 4G <i class="battery"></i></span></div>
  <div class="menu"></div>
  <h1 class="title-left" style="top:47px;font-style:normal;font-weight:700;font-size:11.5px">PathMentor Tracker</h1>
  <div class="sub abs" style="left:15px;top:64px">December 30, Tuesday</div>
  <div class="viewall" style="top:64px">View all ›</div>
  <div class="yellow-card" style="left:15px;top:81px;width:81px;height:63px;text-align:center">
    <svg style="width:18px;height:18px;margin-top:10px;color:var(--ink)"><use href="#i-cal"/></svg>
    <div style="font-size:13px;font-weight:800;font-style:italic;line-height:1.1">271</div>
    <div style="font-size:3.8px;font-style:italic">Weekly Reports</div>
  </div>
  <div class="grey-card" style="left:105px;top:81px;width:81px;height:63px;text-align:center">
    <svg style="width:18px;height:18px;margin-top:10px;color:var(--ink)"><use href="#i-cal-grid"/></svg>
    <div style="font-size:13px;font-weight:800;font-style:italic;line-height:1.1">75</div>
    <div style="font-size:3.8px;font-style:italic">Monthly Reports</div>
  </div>
  <div class="grey-card" style="left:15px;top:156px;width:171px;height:108px;background:linear-gradient(160deg,#b5b2ae,#7d7b79)">
    <div class="abs" style="left:13px;top:9px;font-size:8px;font-weight:800;font-style:italic;color:#fff">Your Overall Progress</div>
    <div class="abs" style="right:13px;top:9px;text-align:right;color:#fff">
      <div style="font-size:3.6px;font-style:italic">Weekly Average</div>
      <div style="font-size:8px;font-weight:800;font-style:italic">Lorem Ips</div>
    </div>
    <div class="abs" style="left:13px;right:13px;top:29px;height:61px;display:flex;justify-content:space-between;align-items:flex-end">
      <i style="width:9px;height:61px;border-radius:5px;background:rgba(255,255,255,.25);display:flex;align-items:flex-end"><b style="width:100%;height:28px;border-radius:5px;background:#fff"></b></i>
      <i style="width:9px;height:61px;border-radius:5px;background:rgba(255,255,255,.25);display:flex;align-items:flex-end"><b style="width:100%;height:34px;border-radius:5px;background:#fff"></b></i>
      <i style="width:9px;height:61px;border-radius:5px;background:rgba(255,255,255,.25);display:flex;align-items:flex-end"><b style="width:100%;height:26px;border-radius:5px;background:#fff"></b></i>
      <i style="width:9px;height:61px;border-radius:5px;background:rgba(255,255,255,.25);display:flex;align-items:flex-end"><b style="width:100%;height:22px;border-radius:5px;background:#fff"></b></i>
      <i style="width:9px;height:61px;border-radius:5px;background:rgba(255,255,255,.25);display:flex;align-items:flex-end"><b style="width:100%;height:19px;border-radius:5px;background:#fff"></b></i>
      <i style="width:9px;height:61px;border-radius:5px;background:rgba(255,255,255,.25);display:flex;align-items:flex-end"><b style="width:100%;height:17px;border-radius:5px;background:#fff"></b></i>
      <i style="width:9px;height:61px;border-radius:5px;background:rgba(255,255,255,.25);display:flex;align-items:flex-end"><b style="width:100%;height:25px;border-radius:5px;background:#fff"></b></i>
      <i style="width:9px;height:61px;border-radius:5px;background:rgba(255,255,255,.25);display:flex;align-items:flex-end"><b style="width:100%;height:20px;border-radius:5px;background:#fff"></b></i>
      <i style="width:9px;height:61px;border-radius:5px;background:rgba(255,255,255,.25);display:flex;align-items:flex-end"><b style="width:100%;height:22px;border-radius:5px;background:#fff"></b></i>
      <i style="width:9px;height:61px;border-radius:5px;background:rgba(255,255,255,.25);display:flex;align-items:flex-end"><b style="width:100%;height:22px;border-radius:5px;background:#fff"></b></i>
      <i style="width:9px;height:61px;border-radius:5px;background:rgba(255,255,255,.25);display:flex;align-items:flex-end"><b style="width:100%;height:20px;border-radius:5px;background:#fff"></b></i>
      <i style="width:9px;height:61px;border-radius:5px;background:rgba(255,255,255,.25);display:flex;align-items:flex-end"><b style="width:100%;height:21px;border-radius:5px;background:#fff"></b></i>
    </div>
    <div class="abs" style="left:13px;right:13px;top:94px;display:flex;justify-content:space-between;font-size:4.2px;font-style:italic;color:#eee">
      <span>45</span><span>55</span><span>42</span><span>38</span><span>32</span><span>30</span><span>41</span><span>35</span><span>38</span><span>38</span><span>34</span><span>37</span>
    </div>
  </div>
  <div class="abs" style="left:15px;top:281px;font-size:8px;font-weight:800;font-style:italic">Your Growth</div>
  <div class="viewall" style="top:284px">View all ›</div>
  <div class="abs" role="img" aria-label="Photo of a person wading in a river, tinted yellow" style="left:15px;top:301px;width:171px;height:60px;border-radius:10px 10px 0 0;background:linear-gradient(135deg,#fff36a 0%,#f3d400 55%,#d9b800 100%)">
    <div class="abs" style="left:16px;top:15px;width:150px;font-size:8px;line-height:1.25;font-weight:800;font-style:italic;color:var(--ink)">BODY: Did I take a cold shower or swim in the river today?</div>
    <div class="abs" style="left:16px;top:37px;font-size:3.8px;font-style:italic;color:var(--ink)">8-10 MIN</div>
  </div>
</section>

<section class="screen" style="left:725px;top:37px">
  <div class="status"><span>7.00 PM</span><span class="net">▂▄▆ 4G <i class="battery"></i></span></div>
  <div class="menu"></div>
  <h1 class="title-left" style="top:47px;font-size:13px">Balance</h1>
  <div class="sub abs" style="left:19px;top:64px">What was focus in family activities?</div>
  <div class="viewall" style="top:64px">View all ›</div>
  <div class="yellow-card" style="left:14px;top:84px;width:171px;height:114px">
    <div class="abs" style="left:13px;top:12px;font-size:8px;font-weight:800;font-style:italic">81 kg<div style="font-size:3.6px;font-weight:400">Started Weight</div></div>
    <div class="abs" style="right:12px;top:12px;text-align:right;font-size:8px;font-weight:800;font-style:italic">75 kg<div style="font-size:3.6px;font-weight:400">Targeted Weight</div></div>
  </div>
  <svg class="abs" style="left:0;top:0" width="200" height="355" viewBox="0 0 200 355" aria-label="Weight trend from January to June">
    <g stroke="#1a1a1a" stroke-width=".6">
      <line x1="26" y1="123" x2="174" y2="123"/><line x1="26" y1="134" x2="174" y2="134"/>
      <line x1="26" y1="145" x2="174" y2="145"/><line x1="26" y1="156" x2="174" y2="156"/>
      <line x1="26" y1="167" x2="174" y2="167"/><line x1="26" y1="178" x2="174" y2="178"/>
    </g>
    <polyline points="28,135 58,146 85,146 113,157 141,157 168,168" fill="none" stroke="#111" stroke-width="1"/>
    <g fill="#111"><circle cx="28" cy="135" r="2.4"/><circle cx="58" cy="146" r="2.4"/><circle cx="85" cy="146" r="2.4"/><circle cx="113" cy="157" r="2.4"/><circle cx="141" cy="157" r="2.4"/><circle cx="168" cy="168" r="2.4"/></g>
    <g font-size="4.4" font-family="Poppins,Arial,sans-serif" font-style="italic" fill="#111" text-anchor="middle">
      <text x="35" y="189">JAN</text><text x="62" y="189">FEB</text><text x="90" y="189">MAR</text><text x="117" y="189">APR</text><text x="145" y="189">MAY</text><text x="172" y="189">JUN</text>
    </g>
  </svg>
  <h2 class="abs" style="left:18px;top:213px;font-size:12.5px;font-weight:800;font-style:italic">Discover</h2>
  <p class="abs" style="left:18px;top:233px;width:166px;font-size:4.4px;line-height:1.6">Lorem ipsum dolor sit amet, consectetuer adipiscing elit, sed diam nonummy nibh euismod tincidunt ut laoreet dolore magna aliquam erat volutpat. Ut wisi enim ad minim veniam, quis nostrud exerci tation ullamcorper suscipit lobortis nisl ut aliquip ex ea commodo consequat.</p>
  <p class="abs" style="left:18px;top:277px;width:166px;font-size:4.4px;line-height:1.6">Duis autem vel eum iriure dolor in hendrerit in vulputate velit esse molestie consequat, vel illum dolore eu feugiat nulla facilisis at vero eros et accumsan et iusto odio dignissim qui blandit praesent lupta-tum zzril delenit augue duis dolore te feugait nulla facilisi.</p>
  <nav class="nav">
    <div class="nav-item"><svg><use href="#i-home"/></svg><span>HOME</span></div>
    <div class="nav-item"><svg><use href="#i-questions"/></svg><span>QUESTIONS</span></div>
    <div class="nav-item"><svg><use href="#i-game"/></svg><span>GAMIFICATION</span></div>
    <div class="nav-item"><svg><use href="#i-people"/></svg><span>SOCIAL CHAT</span></div>
    <div class="nav-item"><svg><use href="#i-more"/></svg><span>MORE</span></div>
  </nav>
</section>

<!-- ============ ROW 2 ============ -->

<section class="screen" style="left:37px;top:422px">
  <div class="status"><span>7.00 PM</span><span class="net">▂▄▆ 4G <i class="battery"></i></span></div>
  <h1 class="title" style="top:39px">REPORTS</h1>
  <div class="abs" style="left:65px;top:58px;display:flex;gap:2px;font-size:5.6px;font-style:italic;line-height:1.5">
    <span style="background:#fff;color:#111;border-radius:6px;padding:1px 7px">Weekly</span>
    <span style="border:1px solid #aaa;border-radius:6px;padding:0 5px">Monthly</span>
  </div>
  <div class="dots" style="left:37px;top:133px;height:27px"></div>
  <div class="dots" style="left:37px;top:192px;height:28px"></div>
  <div class="dots" style="left:37px;top:252px;height:27px"></div>
  <div class="dots" style="left:37px;top:311px;height:10px"></div>
  <div class="day" style="left:21px;top:101px">22</div>
  <div class="day" style="left:21px;top:160px">21</div>
  <div class="day" style="left:21px;top:220px">20</div>
  <div class="day" style="left:21px;top:279px">19</div>
  <div class="grey-card" style="left:66px;top:86px;width:112px;height:45px;padding:7px 9px"><span class="time-pill">18:00–21:00</span><div class="card-text">Lorem ipsum dolor<br>sitamet, consectetuer</div></div>
  <div class="grey-card" style="left:66px;top:145px;width:112px;height:45px;padding:7px 9px"><span class="time-pill">18:00–21:00</span><div class="card-text">Lorem ipsum dolor<br>sitamet, consectetuer</div></div>
  <div class="grey-card" style="left:66px;top:204px;width:112px;height:45px;padding:7px 9px"><span class="time-pill">18:00–21:00</span><div class="card-text">Lorem ipsum dolor<br>sitamet, consectetuer</div></div>
  <div class="grey-card" style="left:66px;top:263px;width:112px;height:45px;padding:7px 9px"><span class="time-pill">18:00–21:00</span><div class="card-text">Lorem ipsum dolor<br>sitamet, consectetuer</div></div>
  <nav class="nav">
    <div class="nav-item"><svg><use href="#i-home"/></svg><span>HOME</span></div>
    <div class="nav-item"><svg><use href="#i-questions"/></svg><span>QUESTIONS</span></div>
    <div class="nav-item"><svg><use href="#i-game"/></svg><span>GAMIFICATION</span></div>
    <div class="nav-item"><svg><use href="#i-people"/></svg><span>SOCIAL CHAT</span></div>
    <div class="nav-item"><svg><use href="#i-more"/></svg><span>MORE</span></div>
  </nav>
</section>

<section class="screen fade-up" style="left:267px;top:422px">
  <div class="status"><span>7.00 PM</span><span class="net">▂▄▆ 4G <i class="battery"></i></span></div>
  <h1 class="title" style="top:46px">Daily Questions</h1>
  <p class="abs" style="left:16px;right:16px;top:66px;text-align:center;font-size:6.3px;line-height:1.45">You already filled out all your questions. You will receive a push notification when you can fill out your next questionnaire.</p>
  <svg class="abs" style="left:82px;top:104px" width="34" height="30" viewBox="0 0 34 30" aria-label="Thumbs up">
    <path d="M4 12h7l3-9c3 0 4 2 4 4l-1 5h7c2 0 3 2 2 4l-2 9c0 2-2 3-4 3H4z M24 13h6v15h-6" fill="none" stroke="#ffd600" stroke-width="1.6" stroke-linejoin="round"/>
    <path d="M4 17h6M4 22h6" stroke="#ffd600" stroke-width="1.3"/>
  </svg>
  <nav class="nav">
    <div class="nav-item"><svg><use href="#i-home"/></svg><span>HOME</span></div>
    <div class="nav-item"><svg><use href="#i-questions"/></svg><span>QUESTIONS</span></div>
    <div class="nav-item"><svg><use href="#i-game"/></svg><span>GAMIFICATION</span></div>
    <div class="nav-item"><svg><use href="#i-people"/></svg><span>SOCIAL CHAT</span></div>
    <div class="nav-item"><svg><use href="#i-more"/></svg><span>MORE</span></div>
  </nav>
</section>

<section class="screen" style="left:496px;top:422px">
  <div class="status"><span>7.00 PM</span><span class="net">▂▄▆ 4G <i class="battery"></i></span></div>
  <h1 class="title" style="top:40px">Verbatims</h1>
  <div class="dots" style="left:37px;top:110px;height:39px"></div>
  <div class="dots" style="left:37px;top:181px;height:38px"></div>
  <div class="dots" style="left:37px;top:251px;height:39px"></div>
  <div class="day" style="left:21px;top:78px">22</div>
  <div class="day" style="left:21px;top:149px">21</div>
  <div class="day" style="left:21px;top:219px">20</div>
  <div class="day" style="left:21px;top:290px">19</div>
  <div class="grey-card" style="left:66px;top:63px;width:112px;height:61px;padding:7px 9px"><div style="font-size:5.8px">05/27/2025</div><div class="card-text" style="font-weight:500;margin-top:2px">Lorem ipsum dolor<br>sitamet, consectetuer</div><span class="show">SHOW REPORT</span><span class="badge-num">28</span></div>
  <div class="grey-card" style="left:66px;top:134px;width:112px;height:61px;padding:7px 9px"><div style="font-size:5.8px">05/19/2025</div><div class="card-text" style="font-weight:500;margin-top:2px">Lorem ipsum dolor<br>sitamet, consectetuer</div><span class="show">SHOW REPORT</span><span class="badge-num">41</span></div>
  <div class="grey-card" style="left:66px;top:205px;width:112px;height:61px;padding:7px 9px"><div style="font-size:5.8px">05/15/2025</div><div class="card-text" style="font-weight:500;margin-top:2px">Lorem ipsum dolor<br>sitamet, consectetuer</div><span class="show">SHOW REPORT</span><span class="badge-num">45</span></div>
  <div class="grey-card" style="left:66px;top:275px;width:112px;height:61px;padding:7px 9px"><div style="font-size:5.8px">05/13/2025</div><div class="card-text" style="font-weight:500;margin-top:2px">Lorem ipsum dolor<br>sitamet, consectetuer</div><span class="badge-num">45</span></div>
  <nav class="nav">
    <div class="nav-item"><svg><use href="#i-home"/></svg><span>HOME</span></div>
    <div class="nav-item"><svg><use href="#i-questions"/></svg><span>QUESTIONS</span></div>
    <div class="nav-item"><svg><use href="#i-game"/></svg><span>GAMIFICATION</span></div>
    <div class="nav-item"><svg><use href="#i-people"/></svg><span>SOCIAL CHAT</span></div>
    <div class="nav-item"><svg><use href="#i-more"/></svg><span>MORE</span></div>
  </nav>
</section>

<section class="screen fade-up" style="left:725px;top:422px">
  <div class="status"><span>7.00 PM</span><span class="net">▂▄▆ 4G <i class="battery"></i></span></div>
  <h1 class="title" style="top:46px">More</h1>
  <p class="abs" style="left:14px;right:14px;top:66px;text-align:center;font-size:6.3px;line-height:1.45">Lorem ipsum dolor sit amet, consectetuer adipiscing elit, sed diam nonummy nibh euismod tincidunt ut laoreet.</p>
  <div class="abs" style="left:37px;top:105px;width:60px;height:19px;border:1px solid var(--yellow);border-radius:10px;text-align:center;line-height:17px;font-size:6px;font-weight:600">VERBATIMS</div>
  <div class="btn" style="left:104px;top:105px;width:59px;height:19px;line-height:19px;font-size:6px">SIGN OUT</div>
  <nav class="nav">
    <div class="nav-item"><svg><use href="#i-home"/></svg><span>HOME</span></div>
    <div class="nav-item"><svg><use href="#i-questions"/></svg><span>QUESTIONS</span></div>
    <div class="nav-item"><svg><use href="#i-game"/></svg><span>GAMIFICATION</span></div>
    <div class="nav-item"><svg><use href="#i-people"/></svg><span>SOCIAL CHAT</span></div>
    <div class="nav-item"><svg><use href="#i-more"/></svg><span>MORE</span></div>
  </nav>
</section>

<!-- ============ ROW 3 ============ -->

<section class="screen" style="left:37px;top:807px">
  <div class="status"><span>7.00 PM</span><span class="net">▂▄▆ 4G <i class="battery"></i></span></div>
  <h1 class="title" style="top:46px">MESSAGES</h1>
  <div class="msg-card" style="top:77px"><i class="avatar" role="img" aria-label="Profile photo"></i><b>Kate, 32</b><p>Lorem ipsum dolor sit amet?<br>Consectetuer! adipiscing...</p></div>
  <div class="msg-card" style="top:136px"><i class="avatar" role="img" aria-label="Profile photo"></i><b>Kate, 32</b><p>Lorem ipsum dolor sit amet?<br>Consectetuer! adipiscing...</p></div>
  <div class="msg-card" style="top:195px"><i class="avatar" role="img" aria-label="Profile photo"></i><b>Kate, 32</b><p>Lorem ipsum dolor sit amet?<br>Consectetuer! adipiscing...</p></div>
  <div class="msg-card" style="top:254px"><i class="avatar" role="img" aria-label="Profile photo"></i><b>Kate, 32</b><p>Lorem ipsum dolor sit amet?<br>Consectetuer! adipiscing...</p></div>
  <div class="abs" style="left:161px;top:277px;width:26px;height:26px;border-radius:50%;background:var(--yellow);color:var(--ink);font-size:17px;font-weight:300;text-align:center;line-height:25px">+</div>
  <div class="abs" style="left:196px;top:50px;width:2px;height:265px;background:#333"><i style="display:block;margin-top:215px;height:26px;background:#fff"></i></div>
  <nav class="nav plain">
    <div class="nav-item"><svg><use href="#i-home"/></svg></div>
    <div class="nav-item"><svg><use href="#i-heart"/></svg></div>
    <div class="nav-item"><svg><use href="#i-chat"/></svg></div>
    <div class="nav-item"><svg><use href="#i-user"/></svg></div>
  </nav>
</section>

<section class="screen" style="left:267px;top:807px">
  <div class="status"><span>7.00 PM</span><span class="net">▂▄▆ 4G <i class="battery"></i></span></div>
  <i class="avatar abs" role="img" aria-label="Profile photo of Kate" style="left:83px;top:31px;width:35px;height:35px"></i>
  <h1 class="title" style="top:70px;font-size:12px">Kate, 32</h1>
  <div class="abs" style="left:0;right:0;top:87px;text-align:center;font-size:7.5px;color:var(--yellow)">Online</div>
  <div class="bubble" style="left:18px;top:104px;width:107px;height:27px">Lorem ipsum dolor sit amet?<br>Consectetuer! adipiscing...<small>14:30</small></div>
  <div class="bubble" style="left:105px;top:143px;width:76px;height:20px">Yes! dolor sit amet? :P<small>14:30</small></div>
  <div class="bubble" style="left:18px;top:174px;width:107px;height:27px">Lorem ipsum dolor sit amet?<br>Consectetuer! adipiscing...<small>14:30</small></div>
  <div class="bubble" style="left:105px;top:212px;width:76px;height:20px">Thank U! <span style="color:#e0245e">♥ ♥</span><small>14:30</small></div>
  <div class="bubble" style="left:15px;top:236px;width:38px;height:17px;text-align:center;color:#888;padding:3px">• • •</div>
  <div class="abs" style="left:0;right:0;top:264px;border-top:1px solid #222"></div>
  <div class="abs" style="left:15px;top:278px;width:131px;height:27px;border-radius:4px;background:#efebe8;color:#555;font-size:8px;line-height:27px;padding-left:11px">Message...</div>
  <div class="btn" style="left:151px;top:278px;width:30px;height:27px;border-radius:3px">
    <svg width="14" height="14" viewBox="0 0 24 24" style="margin-top:6px"><path d="M21 3 3 11l8 2 2 8z" fill="#111"/></svg>
  </div>
  <nav class="nav plain">
    <div class="nav-item"><svg><use href="#i-home"/></svg></div>
    <div class="nav-item"><svg><use href="#i-heart"/></svg></div>
    <div class="nav-item"><svg><use href="#i-chat"/></svg></div>
    <div class="nav-item"><svg><use href="#i-user"/></svg></div>
  </nav>
</section>

<section class="screen" style="left:496px;top:807px">
  <div class="status"><span>7.00 PM</span><span class="net">▂▄▆ 4G <i class="battery"></i></span></div>
  <h1 class="title" style="top:36px">Gamification Overview</h1>
  <div class="abs" style="left:0;right:0;top:53px;text-align:center;font-size:5.8px;font-weight:500">Track your progress and stay motivated</div>
  <div class="yellow-card" style="left:24px;top:65px;width:151px;height:47px">
    <svg class="abs" style="left:11px;top:8px" width="20" height="24" viewBox="0 0 20 24" aria-label="Flame"><path d="M10 1c1 5 8 7 8 14a8 8 0 0 1-16 0c0-4 3-6 3-9 2 2 2 4 2 5 2-2 3-6 3-10z" fill="#f26b1d"/><path d="M10 12c1 3 4 4 4 7a4 4 0 0 1-8 0c0-2 2-3 4-7z" fill="#ffb13b"/></svg>
    <div class="abs" style="left:37px;top:7px;font-size:5.8px;font-weight:600">Current<div style="font-size:10px;font-weight:500;line-height:1.2">12 Days</div></div>
    <div class="abs" style="left:91px;top:7px;font-size:5.8px;font-weight:600">Longest Streak<div style="font-size:10px;font-weight:500;line-height:1.2">27 Days</div></div>
    <div class="abs" style="left:13px;top:37px;width:125px;height:3px;border-radius:2px;background:#fff3a0"><i style="display:block;width:70%;height:100%;border-radius:2px;background:#111"></i></div>
  </div>
  <div class="sec" style="top:119px">Rewards</div>
  <div class="grey-card" style="left:24px;top:134px;width:151px;height:52px">
    <div class="abs" style="left:10px;top:5px;font-size:5.5px;font-weight:500">Next Reward</div>
    <div class="abs" style="left:10px;top:13px;font-size:9.5px;font-weight:500;line-height:1.15;color:#fff">Free Booster in<br>3 more days!</div>
    <div class="abs" style="left:91px;top:15px;width:22px;height:21px;border-radius:3px;background:var(--yellow)"><svg width="22" height="21" viewBox="0 0 22 21" aria-label="Gift"><rect x="5" y="8" width="12" height="9" fill="#111"/><rect x="4" y="6" width="14" height="3" fill="#111"/><rect x="10" y="6" width="2" height="11" fill="#ffd600"/></svg></div>
    <div class="abs" style="left:117px;top:15px;width:22px;height:21px;border-radius:3px;background:var(--yellow)"><svg width="22" height="21" viewBox="0 0 24 24" aria-label="Star"><path d="M12 3l2.7 5.6 6.1.9-4.4 4.3 1 6.1L12 17l-5.4 2.9 1-6.1-4.4-4.3 6.1-.9z" fill="#fff"/></svg></div>
    <div class="abs" style="right:9px;top:42px;font-size:5.5px;font-weight:600">Claimed Rewards</div>
  </div>
  <div class="sec" style="top:192px">Badges</div>
  <div class="grey-card" style="left:25px;top:209px;width:70px;height:77px">
    <div class="badge-ico" style="left:8px;top:5px"><svg width="11" height="11" viewBox="0 0 24 24"><circle cx="12" cy="12" r="9" fill="none" stroke="#ffd600" stroke-width="2"/><path d="M7 12l4 4 7-8" fill="none" stroke="#fff" stroke-width="2.4"/></svg></div>
    <div class="badge-lbl" style="left:3px;top:27px">Consistency<br>Champ</div>
    <div class="badge-ico" style="left:42px;top:5px">7</div>
    <div class="badge-lbl" style="left:37px;top:27px">7-day<br>Streak</div>
    <div class="badge-ico" style="left:8px;top:41px"><svg width="9" height="11" viewBox="0 0 18 22"><path d="M2 1h14M2 21h14M4 1c0 7 10 7 10 10S4 14 4 21M14 1c0 7-10 7-10 10s10 3 10 10" fill="none" stroke="#ffd600" stroke-width="2"/></svg></div>
    <div class="badge-lbl" style="left:3px;top:63px">30-Min<br>Focus Master</div>
    <div class="badge-ico" style="left:42px;top:41px"><svg width="9" height="11" viewBox="0 0 18 22"><rect x="2" y="9" width="14" height="12" rx="2" fill="#fff"/><path d="M5 9V6a4 4 0 0 1 8 0v3" fill="none" stroke="#fff" stroke-width="2"/></svg></div>
    <div class="abs" style="left:50px;top:62px;font-size:7px;font-weight:700">?</div>
  </div>
  <div class="grey-card" style="left:104px;top:209px;width:71px;height:77px;text-align:center">
    <svg class="abs" style="left:15px;top:4px" width="42" height="42" viewBox="0 0 42 42" aria-label="Level progress ring">
      <circle cx="21" cy="21" r="18" fill="none" stroke="#fff" stroke-width="2.5"/>
      <circle cx="21" cy="21" r="18" fill="none" stroke="#ffd600" stroke-width="2.5" stroke-dasharray="73 113" transform="rotate(-90 21 21)"/>
    </svg>
    <div class="abs" style="left:0;right:0;top:14px;font-size:6px;font-weight:500">Level</div>
    <div class="abs" style="left:0;right:0;top:19px;font-size:15px;font-weight:700">4</div>
    <div class="abs" style="left:0;right:0;top:51px;font-size:5.6px;font-weight:600">325/500 XP</div>
    <div class="abs" style="left:8px;top:60px;width:55px;height:2px;background:#fff"><i style="display:block;width:65%;height:100%;background:var(--yellow)"></i></div>
    <div class="abs" style="left:0;right:0;top:65px;font-size:5.6px;font-weight:600">Time Keeper</div>
  </div>
  <div class="btn" style="left:24px;top:294px;width:151px;height:21px;line-height:21px;font-size:7.5px;letter-spacing:1px;font-weight:600">KEEP THE STREAK GOING</div>
  <nav class="nav">
    <div class="nav-item"><svg><use href="#i-home"/></svg><span>HOME</span></div>
    <div class="nav-item"><svg><use href="#i-questions"/></svg><span>QUESTIONS</span></div>
    <div class="nav-item"><svg><use href="#i-game"/></svg><span>GAMIFICATION</span></div>
    <div class="nav-item"><svg><use href="#i-people"/></svg><span>SOCIAL CHAT</span></div>
    <div class="nav-item"><svg><use href="#i-more"/></svg><span>MORE</span></div>
  </nav>
</section>

<section class="screen" style="left:725px;top:807px">
  <div class="status"><span>7.00 PM</span><span class="net">▂▄▆ 4G <i class="battery"></i></span></div>
  <h1 class="title" style="top:38px;line-height:1.25">Keep the<br>Streak Going</h1>
  <div class="abs" role="img" aria-label="Illustration of a calendar page with a flame and a star" style="left:34px;top:85px;width:134px;height:100px;border-radius:14px;background:radial-gradient(circle at 45% 55%,#ff8a2a 0%,#ffc640 30%,#fff3d2 55%,rgba(255,214,0,.35) 75%,rgba(0,0,0,0) 100%)"></div>
  <p class="abs" style="left:10px;right:10px;top:213px;text-align:center;font-size:9.5px;font-weight:300;line-height:1.35">You’re on a 12-day streak.<br>Complete a task today<br>to keep it up!</p>
  <div class="btn" style="left:24px;top:272px;width:151px;height:24px;line-height:24px;font-size:8px;letter-spacing:1px">COMPLETE A TASK</div>
  <nav class="nav">
    <div class="nav-item"><svg><use href="#i-home"/></svg><span>HOME</span></div>
    <div class="nav-item"><svg><use href="#i-questions"/></svg><span>QUESTIONS</span></div>
    <div class="nav-item"><svg><use href="#i-game"/></svg><span>GAMIFICATION</span></div>
    <div class="nav-item"><svg><use href="#i-people"/></svg><span>SOCIAL CHAT</span></div>
    <div class="nav-item"><svg><use href="#i-more"/></svg><span>MORE</span></div>
  </nav>
</section>

</body>
</html>
```